Square graphic for social media post

I want to create a 1080 x 1080px all-black image for the quote below that I can share on social media. I want the emphasis to be primarily on the quote, secondarily on the portrait, and third (smallest) on the logo. I want the background on the portrait to be edited so it's transparent and just shows the face of the person on a black background (no brick wall visible).

Graphic color: black
Text color: white
Content: "What we went through is going to make the greatest generation of hoteliers our industry has ever seen." << biggest text
Dorian Welk << smaller text
President, Marrowgate Hotels << smaller text
[image of person - use whichever version looks better to you]
[Add Lodging Ledger logo - whichever looks better to you]

This image needs to be readable when sized down much smaller (400x400?) so want the text and portrait to take up most of the space.

I'd like the output both as PNG and original file (preferably Canva). Thanks!

Target Market(s)

Hotel managers

Industry/Entity Type

Hospitality

Font styles to use
Sans Serif

Colors

Designer to choose colors to be used in the design.

Requirements
Must have
• Needs to focus on the quote and the person quoted (the portrait)

```html
<!DOCTYPE html>
<html lang="en">
<head>
<meta charset="utf-8">
<title>Quote Card – Dorian Welk</title>
<link href="https://fonts.googleapis.com/css2?family=Domine:wght@700&family=Open+Sans:wght@400&display=swap" rel="stylesheet">
<style>
  :root {
    --bg: #07080b;
    --ink: #ffffff;
    --suit: #1f3f8a;
    --suit-deep: #142b63;
    --shirt: #ece8ea;
    --skin: #d9a88e;
    --hair: #3a3632;
  }
  * { margin: 0; padding: 0; box-sizing: border-box; }
  html, body { width: 1200px; height: 1200px; overflow: hidden; background: var(--bg); }
  .card {
    position: relative;
    width: 1200px;
    height: 1200px;
    background: var(--bg);
    color: var(--ink);
    overflow: hidden;
  }
  .portrait {
    position: absolute;
    left: 0;
    top: 366px;
    width: 944px;
    height: 834px;
  }
  .quote {
    font-family: "Domine", Georgia, serif;
    font-weight: 700;
    font-size: 66px;
    letter-spacing: -0.5px;
    line-height: 1;
    color: var(--ink);
  }
  .quote-line {
    position: absolute;
    white-space: nowrap;
  }
  .quote-line.centered { left: 638px; transform: translateX(-50%); }
  .quote-line.side { left: 709px; }
  .mark {
    position: absolute;
    font-family: "Domine", Georgia, serif;
    font-weight: 700;
    font-size: 210px;
    line-height: 1;
    color: var(--ink);
  }
  .mark.open { left: 64px; top: 58px; }
  .mark.close { left: 890px; top: 660px; }
  .attribution {
    position: absolute;
    left: 708px;
    top: 805px;
  }
  .attribution .name {
    font-family: "Domine", Georgia, serif;
    font-weight: 700;
    font-size: 30px;
    letter-spacing: 0.5px;
    line-height: 1.1;
  }
  .attribution .role {
    font-family: "Open Sans", Arial, sans-serif;
    font-size: 22px;
    line-height: 1.3;
    padding-left: 24px;
    margin-top: 4px;
  }
  .brand {
    position: absolute;
    right: 86px;
    bottom: 70px;
    display: flex;
    flex-direction: column;
    align-items: center;
    gap: 10px;
  }
  .brand-dot {
    width: 46px;
    height: 46px;
    border-radius: 50%;
    background: var(--ink);
  }
  .brand-name {
    font-family: "Domine", Georgia, serif;
    font-weight: 700;
    font-size: 22px;
    color: var(--ink);
    white-space: nowrap;
  }
</style>
</head>
<body>
  <main class="card">
    <svg class="portrait" viewBox="0 0 944 834" role="img" aria-label="Portrait of Dorian Welk, smiling, in a blue blazer and white open-collar shirt, cut out on black">
      <defs>
        <linearGradient id="figureTone" x1="0" y1="0" x2="0" y2="1">
          <stop offset="0" stop-color="var(--hair)"/>
          <stop offset="0.14" stop-color="var(--skin)"/>
          <stop offset="0.6" stop-color="var(--skin)"/>
          <stop offset="0.72" stop-color="var(--shirt)"/>
          <stop offset="0.82" stop-color="var(--suit)"/>
          <stop offset="1" stop-color="var(--suit-deep)"/>
        </linearGradient>
      </defs>
      <path fill="url(#figureTone)" d="M265 160 C270 60 360 0 450 0 C560 0 640 60 650 170 L660 300 C670 420 640 520 610 560 L620 610 C720 640 800 660 860 700 C910 740 935 790 944 834 L0 834 C20 760 90 700 200 660 C250 640 300 620 320 600 L325 560 C280 500 250 420 245 320 Z"/>
    </svg>

    <span class="mark open" aria-hidden="true">&ldquo;</span>
    <blockquote class="quote">
      <span class="quote-line centered" style="top:104px">What we went through is</span>
      <span class="quote-line centered" style="top:184px">going to make the</span>
      <span class="quote-line centered" style="top:262px">greatest generations of</span>
      <span class="quote-line side" style="top:355px">hoteliers</span>
      <span class="quote-line side" style="top:433px">our</span>
      <span class="quote-line side" style="top:517px">industry</span>
      <span class="quote-line side" style="top:594px">has ever</span>
      <span class="quote-line side" style="top:675px">seen.</span>
    </blockquote>
    <span class="mark close" aria-hidden="true">&rdquo;</span>

    <div class="attribution">
      <p class="name">- DORIAN WELK</p>
      <p class="role">President,&nbsp; Marrowgate Hotels</p>
    </div>

    <div class="brand">
      <span class="brand-dot" aria-hidden="true"></span>
      <span class="brand-name">Lodging Ledger</span>
    </div>
  </main>
</body>
</html>
```